Bry Ta's Jar Lable for kids Christmas gifts

Looking to get a wrap around label made for a quart canning jar. I would like it to have my kids head on it also. I was thinking in a silhouette form on both ends of the wrap( added a quick sketch up). We will be canning Pickles and giving them away as gifts this year. Also might be selling a few at a frames market. The brand name is " Bry Ta's" ( at the moment) So if you could think of a cool logo around that would be awesome also. I am an Orange and Black fan but I am up for suggestions also. Do you think this might be something you could help me with?

The second attached graphic is what I would like my kids faces to look similer to. Art wise. The sketch is of what the ends of the labels need to look like. Not a full face but a half of each of there faces on both ends of the lable.

Colors
f78f20
000000
757575

Requirements
Nice to have
• antique lable feel

```html
<!DOCTYPE html>
<html lang="en">
<head>
<meta charset="utf-8">
<title>Bry Ta's Pickle Jar Label</title>
<link rel="stylesheet" href="https://fonts.googleapis.com/css2?family=Arimo:wght@400&display=swap">
<style>
  :root {
    --label-black: #000000;
    --backdrop: #d6d6d6;
    --text-white: #ffffff;
    --hair-grey: #5e5e5e;
    --skin-tone: #f9c39c;
  }
  html, body {
    margin: 0;
    padding: 0;
    width: 1200px;
    height: 960px;
    overflow: hidden;
    background: var(--backdrop);
  }
  .label {
    position: absolute;
    left: 0;
    top: 117px;
    width: 1200px;
    height: 726px;
    background: var(--label-black);
    font-family: "Arimo", Arial, sans-serif;
    color: var(--text-white);
    overflow: hidden;
  }
  .portrait {
    position: absolute;
    left: 21px;
    top: 156px;
    width: 305px;
    height: 454px;
  }
  .side-copy {
    position: absolute;
    left: 229px;
    top: 297px;
    width: 580px;
    margin: 0;
    font-size: 21px;
    line-height: 29px;
    text-align: center;
    transform: rotate(-90deg);
    transform-origin: 290px 66px;
  }
  .brand-name {
    position: absolute;
    left: 766px;
    top: 62px;
    margin: 0;
    font-size: 100px;
    font-weight: 400;
    line-height: 1;
    letter-spacing: -1px;
    white-space: nowrap;
  }
  .front-copy {
    position: absolute;
    left: 746px;
    top: 281px;
    width: 230px;
    margin: 0;
    font-size: 20px;
    line-height: 25.2px;
  }
</style>
</head>
<body>
  <div class="label">
    <svg class="portrait" viewBox="0 0 305 454" role="img" aria-label="Illustrated portrait of a smiling child with curly grey hair">
      <defs>
        <linearGradient id="portrait-tones" x1="0" y1="0" x2="0" y2="1">
          <stop offset="0" stop-color="var(--hair-grey)"/>
          <stop offset="0.45" stop-color="var(--hair-grey)"/>
          <stop offset="0.6" stop-color="var(--skin-tone)"/>
          <stop offset="1" stop-color="var(--skin-tone)"/>
        </linearGradient>
      </defs>
      <rect x="0" y="0" width="305" height="454" rx="140" fill="url(#portrait-tones)"/>
    </svg>

    <p class="side-copy">A pickled cucumber is a cucumber that has been pickled in a brine, vinegar, or other solution and left to ferment for a period of time, by either immersing the cucumbers in an acidic solution or through souring by lacto-fermentation</p>

    <h1 class="brand-name">Bry Ta's</h1>

    <p class="front-copy">A pickled cucumber is a cucumber that has been pickled in a brine, vinegar, or other solution and left to ferment for a period of time, by either immersing the cucumbers in an acidic solution or through souring by lacto-fermentation</p>
  </div>
</body>
</html>
```